Ecommerce site for Bramwell Dovey Company

This is an ecommerce store design and will be based on the xcart ecommerce platform, attached is a design specification and all images to use in the design, you may use any other images you see fit.
This is a new Company so has no logo, if possible please create a logo but if not just use a text based logo in the design this maybe replaced later if required.
We only require a Home page design initially but will also need a category and product page design created, if you can do those also it would be an advantage.
IMPORTANT
We require all designs to be supplied as a full size JPG so we can see the design in detail as the pixel quarry previews are often too small.

```html
<!DOCTYPE html>
<html lang="en">
<head>
<meta charset="utf-8">
<title>Bramwell Dovey – Curtain Tracks</title>
<link rel="stylesheet" href="https://fonts.googleapis.com/css2?family=Oswald:wght@300;400&family=Noto+Sans:wght@400;700&display=swap">
<style>
:root{
  --page-bg:#efefef;
  --sheet:#ffffff;
  --ink:#222222;
  --text:#333333;
  --dark:#1e1e1e;
  --dark-2:#3a3a3a;
  --line:#dcdcdc;
  --item:#ececec;
  --muted:#888888;
  --teal:#1f5f6c;
}
*{margin:0;padding:0;box-sizing:border-box}
html,body{width:960px;height:1200px;overflow:hidden}
body{background:var(--page-bg);font-family:"Noto Sans",sans-serif;color:var(--text);position:relative}
.sheet{position:absolute;left:88px;top:0;width:784px;height:1200px;background:var(--sheet);box-shadow:0 0 6px rgba(0,0,0,.15)}
.abs{position:absolute}
.dark-band{background:linear-gradient(#3a3a3a,#141414);color:#fff}
.top-bar{left:101px;top:0;width:758px;height:21px;border-radius:0 0 6px 6px;font-size:9.5px;text-align:right;padding:4px 12px 0}
.top-bar a{color:#fff;text-decoration:none}
.logo{left:110px;top:46px;font-family:"Noto Sans",sans-serif;font-weight:700;font-size:32px;color:var(--ink);letter-spacing:-.5px}
.cart-head{left:655px;top:35px;width:204px;height:25px;border-radius:6px;font-family:"Oswald",sans-serif;font-size:16px;padding:1px 0 0 33px}
.cart-head svg{position:absolute;left:9px;top:5px}
.cart-total{left:662px;top:71px;font-size:13.5px;color:var(--ink)}
.cart-links{left:655px;top:98px;width:204px;height:19px;background:var(--item);font-size:9.5px;text-align:right;padding:4px 12px 0;color:var(--ink)}
.delivery{left:100px;top:128px;width:759px;height:50px;border-radius:6px}
.delivery h2{position:absolute;left:12px;top:8px;font-family:"Oswald",sans-serif;font-weight:400;font-size:26px;letter-spacing:.2px;white-space:nowrap}
.delivery h2 em{font-weight:300;font-size:19px}
.search{position:absolute;left:523px;top:9px;width:127px;height:32px;background:#fff;border:1px solid #ccc;font-size:11px;color:#aaa;padding:8px 8px}
.search-btn{position:absolute;left:650px;top:9px;width:64px;height:32px;background:#111;font-family:"Oswald",sans-serif;font-size:14px;text-align:center;padding-top:5px}
.nav-group{left:100px;width:196px}
.nav-group h3{height:26px;border-radius:6px;font-family:"Oswald",sans-serif;font-weight:400;font-size:15.5px;padding:1px 12px 0}
.nav-group ul{list-style:none;margin-top:6px;border:1px solid var(--line)}
.nav-group li{height:21px;background:var(--item);border-bottom:2px solid #fff;font-size:12.5px;padding:1px 12px 0;color:var(--ink)}
.promo{left:100px;width:196px;height:96px;border:1px solid var(--line);overflow:hidden;text-align:center;font-family:"Oswald",sans-serif;color:var(--ink)}
.promo .ph{position:absolute;inset:0}
.promo .txt{position:absolute;left:0;right:0;background:rgba(238,238,238,.82);line-height:1.15}
.slider{left:308px;top:204px;width:551px;height:217px;background:linear-gradient(180deg,#c9d3d6 0%,#d8dfe0 28%,#6f9a8c 45%,#1f5f6c 60%,#d9d6cf 100%)}
.slider-shadow{left:320px;top:418px;width:527px;height:38px;background:radial-gradient(ellipse 50% 60% at 50% 0,rgba(0,0,0,.55),rgba(0,0,0,0) 100%)}
.caption{left:500px;top:342px;width:359px;height:42px;background:rgba(30,30,30,.85);color:#fff;font-family:"Oswald",sans-serif;font-weight:300;font-size:19px;padding:6px 14px}
.dots{left:530px;top:401px;display:flex;gap:8px}
.dots span{width:14px;height:14px;border-radius:50%;background:#222}
.dots span.on{background:#fff;border:3px solid #222}
.title{font-family:"Oswald",sans-serif;font-weight:300;color:var(--ink)}
.about-title{left:309px;top:458px;font-size:28px}
.about-text{left:309px;top:506px;width:550px;font-size:10.8px;line-height:13.6px;color:#222}
.cat-title{font-size:20px;top:634px}
.frame{border:1px solid var(--line);padding:4px;background:#fff}
.frame div{width:100%;height:100%}
.footer{left:100px;top:1122px;width:759px;height:30px;border-radius:6px;font-size:11px;padding:7px 10px}
.footer .right{position:absolute;right:11px;top:7px}
.pay{right:101px;top:1166px;display:flex;gap:10px;font-size:9px;font-weight:700;color:#555}
</style>
</head>
<body>
<div class="sheet"></div>

<div class="abs top-bar dark-band"><a href="#">Login</a> &nbsp;|&nbsp; <a href="#">Register</a> &nbsp;|&nbsp; <a href="#">Need help?</a></div>

<div class="abs logo">Bramwell Dovey</div>

<div class="abs cart-head dark-band">
  <svg width="16" height="14" viewBox="0 0 16 14"><path d="M1 4h14l-2 9H3z" fill="none" stroke="#fff" stroke-width="1.4"/><path d="M4 4l3-3M12 4L9 1" stroke="#fff" stroke-width="1.2"/></svg>
  Shopping Cart
</div>
<div class="abs cart-total">0 item(s) - £0.00</div>
<div class="abs cart-links">View Cart | Checkout</div>

<div class="abs delivery dark-band">
  <h2>FREE UK DELIVERY <em>ON ORDERS OVER £100.</em></h2>
  <div class="search">Search for product...</div>
  <div class="search-btn">SEARCH</div>
</div>

<nav>
  <div class="abs nav-group" style="top:203px"><h3 class="dark-band">Quiet Glide Tracks</h3>
    <ul><li>» Subcategory 1</li><li>» Subcategory 2</li><li>» Subcategory 3</li><li>» Subcategory 4</li></ul></div>
  <div class="abs nav-group" style="top:342px"><h3 class="dark-band">Hand operated Tracks</h3>
    <ul><li>» Subcategory 1</li><li>» Subcategory 2</li><li>» Subcategory 3</li><li>» Subcategory 4</li></ul></div>
  <div class="abs nav-group" style="top:481px"><h3 class="dark-band">Cord operated Tracks</h3>
    <ul><li>» Subcategory 1</li><li>» Subcategory 2</li><li>» Subcategory 3</li><li>» Subcategory 4</li></ul></div>
  <div class="abs nav-group" style="top:620px"><h3 class="dark-band">Automated Tracks</h3>
    <ul><li>» Subcategory 1</li><li>» Subcategory 2</li><li>» Subcategory 3</li><li>» Subcategory 4</li></ul></div>
</nav>

<div class="abs promo" style="top:760px">
  <div class="ph" role="img" aria-label="Close-up of a blue measuring tape" style="background:linear-gradient(100deg,#eee 20%,#4d6ed0 45%,#2a47b0 100%)"></div>
  <div class="txt" style="top:26px;padding:2px 0 4px"><div style="font-size:16px">OVER <i>20 YEARS</i> EXPERIENCE</div><div style="font-size:12.5px">MEASURING / MAKING / FITTING</div></div>
</div>
<div class="abs promo" style="top:880px;background:#eee">
  <svg class="abs" style="left:56px;top:0" width="84" height="70"><circle cx="42" cy="32" r="38" fill="#e3b51a"/></svg>
  <div class="txt" style="top:44px;padding:4px 0"><div style="font-size:15px">5 YEARS <i>GUARANTEE</i> ON</div><div style="font-size:15px">ALL QUIET GLIDE PRODUCTS</div></div>
</div>
<div class="abs promo" style="top:1000px">
  <div class="ph" role="img" aria-label="Smiling family group photo" style="background:linear-gradient(180deg,#e8e4e0 0%,#c9a896 45%,#e7c7c4 100%)"></div>
  <div class="txt" style="top:50px;padding:2px 0 4px;background:rgba(238,238,238,.7)"><div style="font-size:16px">FRIENDLY <i>FAMILY RUN</i></div><div style="font-size:16px">BUSINESS</div></div>
</div>

<div class="abs slider" role="img" aria-label="Bright room with teal curtains on ceiling tracks"></div>
<div class="abs slider-shadow"></div>
<div class="abs caption">Slide Description lorem ipsum dolor sit amet</div>
<div class="abs dots"><span class="on"></span><span></span><span></span><span></span></div>

<h1 class="abs title about-title">About the company</h1>
<p class="abs about-text">Lorem ipsum dolor sit amet, consectetur adipiscing elit. Duis et orci urna. Etiam scelerisque dapibus elit eu ultricies. Nullam enim turpis, viverra et elementum quis, congue in nunc. Suspendisse potenti. Nunc erat ante, tempor id accumsan quis, tempor eget dui. Nullam feugiat hendrerit augue, vitae lacinia lorem sodales vel. Pellentesque pulvinar velit in metus iaculis volutpat. Etiam ipsum purus, accumsan sit amet bibendum at, pharetra in velit. Suspendisse a nulla ut nibh vehicula commodo. Vivamus non eros eros, id ullamcorper ipsum. Morbi ut vehicula purus. Sed lacus mi, facilisis sed adipiscing ac, volutpat eu odio. Nulla lobortis malesuada nisi nec pharetra. Sed quis lacus tellus, non luctus mauris. Curabitur arcu turpis, euismod quis pellentesque et, dignissim ut ligula. Vivamus fringilla tortor id nulla euismod tempor.</p>

<h2 class="abs title cat-title" style="left:308px">Quiet Glide Tracks</h2>
<h2 class="abs title cat-title" style="left:497px">Hand operated Tracks</h2>
<h2 class="abs title cat-title" style="left:684px">Cord operated Tracks</h2>

<div class="abs frame" style="left:309px;top:670px;width:174px;height:130px"><div role="img" aria-label="Modern room with sheer white curtains" style="background:linear-gradient(90deg,#444 0%,#d8d8d8 20%,#f2f2f2 70%,#333 95%)"></div></div>
<div class="abs frame" style="left:497px;top:670px;width:174px;height:130px"><div role="img" aria-label="Living room with roman blinds and white sofa" style="background:linear-gradient(180deg,#7f8790 0%,#a7adb5 50%,#6b6f75 100%)"></div></div>
<div class="abs frame" style="left:684px;top:670px;width:174px;height:130px"><div role="img" aria-label="Dining area with cream curtains" style="background:linear-gradient(90deg,#d9cfa8 0%,#efeee8 35%,#c9d1c7 65%,#e6dcb8 100%)"></div></div>

<h2 class="abs title cat-title" style="left:309px;top:809px">Automated Tracks</h2>
<div class="abs frame" style="left:309px;top:845px;width:550px;height:245px"><div role="img" aria-label="Large hall with teal curtains on automated tracks" style="background:linear-gradient(180deg,#dfe3e2 0%,#c3cfcd 20%,#3f7a80 38%,#1f5f6c 62%,#cba683 82%,#e0c7a4 100%)"></div></div>

<footer class="abs footer dark-band">Contact Us | About Us | Terms &amp; Conditions | Privacy<span class="right">Copyright © 2002-2011 Bramwell Dovey</span></footer>
<div class="abs pay"><span>Paywell</span><span>Vantra</span><span>Orbis</span><span>Amberline</span><span>Northway</span></div>
</body>
</html>
```